Calm and Compass Health Flyer (new business startup)

One page...clear enough to be read if faxed. This mental health clinic treats depression/anxiety in kids and adults. It also treats opiate and alcohol addiction. It's in downtown Elmira, NY and the owner of the clinic is from Elmira NY, where it's located. This clinic does not take health insurance, so it charges a low rate of $75 a visit once they pay the $125 starting fee.

Target Market(s)

doctors offices, new patients

Industry/Entity Type

Doctor

Requirements
Must have
• see microsoft word document. pdf is printed on the company letterhead.
Nice to have
• a simplified map would be nice. if you can include the building it would be a plus. The same two fonts were used in the business cards and letter head (kennedy small caps boo*) and Refrigerator Delux.

```html
<!DOCTYPE html>
<html lang="en">
<head>
<meta charset="utf-8">
<title>Calm and Compass Health – Flyer</title>
<link href="https://fonts.googleapis.com/css2?family=Roboto:ital,wght@0,400;0,700;1,400;1,500&family=Roboto+Condensed:wght@400;700&family=Cormorant+SC:wght@500&family=Saira+Condensed:wght@600&display=swap" rel="stylesheet">
<style>
  :root {
    --orange: #f26a38;
    --blue: #29a6df;
    --ink: #2b2b2b;
    --white: #ffffff;
    --rule: #333333;
  }
  * { margin: 0; padding: 0; box-sizing: border-box; }
  html, body { width: 1023px; height: 1200px; overflow: hidden; background: var(--white); }
  .flyer { position: relative; width: 1023px; height: 1200px; background: var(--white); font-family: "Roboto", Arial, sans-serif; color: var(--ink); }

  .brand { position: absolute; top: 0; left: 0; width: 100%; height: 166px; display: flex; align-items: center; justify-content: center; gap: 22px; }
  .brand-dot { width: 70px; height: 70px; border-radius: 50%; background: var(--orange); }
  .brand-name { font-family: "Roboto", Arial, sans-serif; font-weight: 700; font-size: 48px; color: var(--orange); letter-spacing: -0.5px; }

  .name-band { position: absolute; top: 166px; left: 0; width: 100%; height: 118px; background: var(--blue); color: var(--white); text-align: center; }
  .practitioner { font-family: "Cormorant SC", Georgia, serif; font-weight: 500; font-size: 60px; line-height: 1; padding-top: 14px; letter-spacing: 0.5px; }
  .credential { font-family: "Saira Condensed", "Arial Narrow", sans-serif; font-weight: 600; font-size: 31px; letter-spacing: 4px; margin-top: 4px; }

  .hours { position: absolute; top: 306px; left: 0; width: 100%; text-align: center; font-family: "Roboto Condensed", "Arial Narrow", sans-serif; font-size: 54px; color: var(--orange); line-height: 64px; }
  .hours strong { font-weight: 700; margin-right: 18px; }

  .fees { position: absolute; top: 391px; left: 76px; width: 871px; height: 175px; background: var(--orange); border-radius: 4px; color: var(--white); font-weight: 700; padding: 14px 0 0 38px; }
  .fee-row { display: flex; font-size: 38px; line-height: 48px; }
  .fee-row .service { width: 665px; }
  .fee-row .price { width: 120px; text-align: right; }
  .ages { font-size: 36px; line-height: 56px; margin-left: 4px; }

  .conditions-title { position: absolute; top: 590px; left: 0; width: 100%; display: flex; align-items: center; justify-content: center; gap: 8px; }
  .conditions-title .line { width: 112px; height: 1.5px; background: var(--rule); }
  .conditions-title h2 { font-family: "Roboto Condensed", "Arial Narrow", sans-serif; font-weight: 700; font-size: 42px; color: var(--orange); }

  .conditions { position: absolute; top: 645px; left: 0; width: 100%; text-align: center; font-size: 33px; line-height: 42px; color: var(--ink); }
  .sep { display: inline-block; width: 14px; height: 14px; border-radius: 50%; border: 3px solid var(--orange); margin: 0 6px 4px; vertical-align: middle; }

  .tagline { position: absolute; top: 750px; left: 0; width: 100%; text-align: center; font-style: italic; font-weight: 500; font-size: 24px; color: var(--ink); }
  .disclaimer { position: absolute; top: 784px; left: 66px; width: 891px; text-align: center; font-size: 19px; line-height: 23px; color: var(--ink); }

  .media { position: absolute; top: 861px; height: 265px; border: 1.5px solid #555; }
  .media.building { left: 31px; width: 446px; background: linear-gradient(180deg, #8fb8e8 0%, #a9c7ea 28%, #7a4432 42%, #6a3a2c 82%, #8a8a8a 100%); }
  .media.map { left: 515px; width: 449px; background: linear-gradient(180deg, #ecebe8 0%, #ecebe8 55%, #b8dcf2 62%, #ecebe8 70%, #e6e5e2 100%); }

  .footer { position: absolute; top: 1144px; left: 0; width: 100%; height: 56px; background: var(--blue); color: var(--white); display: flex; align-items: center; justify-content: center; gap: 8px; font-size: 25px; }
  .footer svg { width: 22px; height: 22px; fill: var(--white); }
  .footer .item { display: flex; align-items: center; gap: 5px; }
</style>
</head>
<body>
<main class="flyer">
  <header class="brand">
    <span class="brand-dot"></span>
    <span class="brand-name">CALM &amp; COMPASS HEALTH</span>
  </header>

  <section class="name-band">
    <h1 class="practitioner">DANIEL REYES, RPA, PLLC</h1>
    <p class="credential">Psychiatric Physician Assistant (PA-C-CAQ)</p>
  </section>

  <p class="hours"><strong>Hours:</strong>Monday &amp; Saturdays 9-4 pm</p>

  <section class="fees">
    <div class="fee-row"><span class="service">Psychiatric Evaluation&nbsp; (45min) -</span><span class="price">$125*</span></div>
    <div class="fee-row"><span class="service">Psychiatric Office Visit (15min) -</span><span class="price">$75*</span></div>
    <p class="ages">AGES:&nbsp; 6 YEARS OLD AND UP</p>
  </section>

  <div class="conditions-title">
    <span class="line"></span>
    <h2>CONDITIONS TREATED</h2>
    <span class="line"></span>
  </div>

  <p class="conditions">
    Depression<span class="sep"></span>Anxiety<span class="sep"></span>PTSD<span class="sep"></span>ADHD<span class="sep"></span>Addiction<br>
    Bipolar<span class="sep"></span>Childhood Mood Disorders
  </p>

  <p class="tagline">We work for you, not the insurance companies</p>
  <p class="disclaimer">*Although we do not partner with any Health Insurance Companies at this time, a bill will be provided to you at the time of service for you to submit&nbsp; to your insurance company.</p>

  <div class="media building" role="img" aria-label="Photo of the red-brick downtown office building housing the clinic"></div>
  <div class="media map" role="img" aria-label="Street map of the downtown area showing the clinic location near the river"></div>

  <footer class="footer">
    <span class="item">42 W. Church St #310, Maple Falls, NY 10987</span>
    <span class="item">
      <svg viewBox="0 0 24 24" aria-hidden="true"><path d="M6.6 10.8a15.1 15.1 0 0 0 6.6 6.6l2.2-2.2c.3-.3.7-.4 1-.2 1.1.4 2.3.6 3.6.6.6 0 1 .4 1 1V20c0 .6-.4 1-1 1A17 17 0 0 1 3 4c0-.6.4-1 1-1h3.5c.6 0 1 .4 1 1 0 1.3.2 2.5.6 3.6.1.3 0 .7-.2 1z"/></svg>
      607-555-0142
    </span>
    <span class="item">
      <svg viewBox="0 0 24 24" aria-hidden="true"><path d="M6 3h12v5H6zM4 9h16a2 2 0 0 1 2 2v6h-4v4H6v-4H2v-6a2 2 0 0 1 2-2zm4 7v3h8v-3z"/></svg>
      607-555-0187
    </span>
  </footer>
</main>
</body>
</html>
```